BPH Business Card 2018

Brellmore Chiropractic. We have two locations that we want to advertise on the same card. Calderwick OrthoAxis campus address: 3815 Pemberly Dr., Suite 240, Flowood, MS 39587. Madison address: 426 Larkmoor Dr., Building D., Madison, MS 39674. website: www.drbrellmore.example. o:(601)555-0148 f:(601)555-0173

Target Market(s)

Health care decision makers: primary care doctors and mothers

Contact Information for Business Card

I have no idea; up for any suggestions and I'd do much better picking from examples versus describing what I'm looking for. We are in a very high end location and would like the cards to look really sharp.

Requirements
Must have
• My name, Tobias R Venmark, D.C.

```html
<!DOCTYPE html>
<html lang="en">
<head>
<meta charset="utf-8">
<title>Brellmore Chiropractic – Business Card</title>
<link rel="stylesheet" href="https://fonts.googleapis.com/css2?family=Cormorant+Garamond:wght@600&family=Work+Sans:wght@400;500&display=swap">
<style>
  :root {
    --backdrop: #2b2b2d;
    --card: #1b1b1c;
    --card-edge: #232325;
    --ink: #f4f4f4;
    --ink-soft: #d9d9d9;
    --rule: #e6e6e6;
  }
  * { box-sizing: border-box; margin: 0; padding: 0; }
  html, body {
    width: 1200px; height: 900px; overflow: hidden;
    background: var(--backdrop);
  }
  .sheet {
    width: 1200px; height: 900px;
    display: flex; flex-direction: column; align-items: center; justify-content: center;
    gap: 40px;
  }
  .card {
    position: relative;
    width: 720px; height: 400px;
    background: linear-gradient(135deg, var(--card-edge) 0%, var(--card) 60%);
    box-shadow: 0 10px 30px rgba(0,0,0,.45);
    color: var(--ink);
  }
  .brand {
    font-family: "Cormorant Garamond", serif;
    font-weight: 600;
    color: var(--ink);
    text-transform: uppercase;
    display: flex; flex-direction: column;
  }
  .brand__mark {
    display: flex; align-items: center; gap: 14px;
  }
  .brand__dot {
    width: 14px; height: 14px; border-radius: 50%; background: var(--ink);
  }
  .brand__name { line-height: 1; letter-spacing: .02em; }
  .brand__campus {
    font-family: "Cormorant Garamond", serif;
    font-weight: 600; text-transform: none; color: var(--ink-soft);
  }
  .brand__address {
    font-family: "Cormorant Garamond", serif;
    font-weight: 600; color: var(--ink-soft); letter-spacing: .04em;
  }

  /* Front */
  .card--front .brand {
    position: absolute; left: 220px; top: 120px;
  }
  .card--front .brand__name { font-size: 44px; }
  .card--front .brand__name-second { font-size: 30px; letter-spacing: .06em; margin-left: 28px; margin-top: 4px; }
  .card--front .brand__campus { font-size: 18px; margin-left: 28px; margin-top: 4px; }
  .card--front .brand__address { font-size: 9px; margin-left: 28px; margin-top: 4px; }

  /* Back */
  .card--back .brand {
    position: absolute; left: 48px; top: 140px;
  }
  .card--back .brand__name { font-size: 32px; }
  .card--back .brand__dot { width: 11px; height: 11px; }
  .card--back .brand__name-second { font-size: 22px; letter-spacing: .06em; margin-left: 25px; margin-top: 3px; }
  .card--back .brand__campus { font-size: 13px; margin-left: 25px; margin-top: 3px; }
  .card--back .brand__address { font-size: 7px; margin-left: 25px; margin-top: 3px; }

  .divider {
    position: absolute; left: 376px; top: 72px;
    width: 2px; height: 256px; background: var(--rule);
  }
  .contact {
    position: absolute; left: 404px; top: 80px;
    font-family: "Work Sans", sans-serif; color: var(--ink);
  }
  .contact__name { font-size: 20px; font-weight: 500; letter-spacing: .03em; text-transform: uppercase; }
  .contact__role { font-size: 15px; margin-top: 2px; color: var(--ink-soft); }
  .contact__address { font-size: 15px; line-height: 1.45; margin-top: 18px; letter-spacing: .02em; }
  .contact__list { list-style: none; margin-top: 12px; }
  .contact__item { display: flex; align-items: center; gap: 10px; font-size: 16px; line-height: 1.55; letter-spacing: .02em; }
  .contact__icon { width: 12px; height: 12px; flex: none; }
</style>
</head>
<body>
<main class="sheet">

  <section class="card card--front" aria-label="Card front">
    <div class="brand">
      <div class="brand__mark">
        <span class="brand__dot"></span>
        <span class="brand__name">Brellmore</span>
      </div>
      <span class="brand__name brand__name-second">Chiropractic</span>
      <span class="brand__campus">Calderwick Professional Campus</span>
      <span class="brand__address">3815 PEMBERLY DRIVE, SUITE 240 &nbsp;FLOWOOD, MS 39587</span>
    </div>
  </section>

  <section class="card card--back" aria-label="Card back">
    <div class="brand">
      <div class="brand__mark">
        <span class="brand__dot"></span>
        <span class="brand__name">Brellmore</span>
      </div>
      <span class="brand__name brand__name-second">Chiropractic</span>
      <span class="brand__campus">Calderwick Professional Campus</span>
      <span class="brand__address">3815 PEMBERLY DRIVE, SUITE 240 &nbsp;FLOWOOD, MS 39587</span>
    </div>

    <div class="divider"></div>

    <div class="contact">
      <p class="contact__name">Tobias R Venmark, D.C.</p>
      <p class="contact__role">Director</p>
      <p class="contact__address">426 Larkmoor Dr., Building D.,<br>Madison, MS 39674.</p>
      <ul class="contact__list">
        <li class="contact__item">
          <svg class="contact__icon" viewBox="0 0 12 12" aria-hidden="true"><path d="M2.5 1 L4.5 1 L5.2 3.5 L4 4.4 Q5 6.8 7.6 8 L8.5 6.8 L11 7.5 L11 9.5 Q10.5 11 9 11 Q1 10.5 1 3 Q1 1.5 2.5 1 Z" fill="#f4f4f4"/></svg>
          <span>(601)555-0148</span>
        </li>
        <li class="contact__item">
          <svg class="contact__icon" viewBox="0 0 12 12" aria-hidden="true"><rect x="3" y="1" width="6" height="3" fill="#f4f4f4"/><rect x="1" y="4.5" width="10" height="4.5" rx="1" fill="#f4f4f4"/><rect x="3" y="8" width="6" height="3" fill="#f4f4f4"/></svg>
          <span>(601)555-0173</span>
        </li>
        <li class="contact__item">
          <svg class="contact__icon" viewBox="0 0 12 12" aria-hidden="true"><circle cx="6" cy="6" r="5" fill="none" stroke="#f4f4f4" stroke-width="1.1"/><ellipse cx="6" cy="6" rx="2.2" ry="5" fill="none" stroke="#f4f4f4" stroke-width="1"/><line x1="1" y1="6" x2="11" y2="6" stroke="#f4f4f4" stroke-width="1"/></svg>
          <span>www.drbrellmore.example</span>
        </li>
      </ul>
    </div>
  </section>

</main>
</body>
</html>
```